Broschüren-Design für Bettenmanufaktur
Super Design, super schnelle Reaktion, super netter Kontakt!
Zielgruppe
Wir sind eine Bettenmanufaktur die Futonbetten und Himmelbetten aus Metall herstellt, geziert mit Leder- oder Holzelementen an den Bettseiten und Rückenlehnen. Das besondere ist, dass es Systembetten sind. Man kann später aus seinen Futonbett noch ein Himmelbett machen, oder die Leder- und Holzelemente einfach tauschen. Unsere Zielgruppe sind Paare die auf Design und Still stehen, sowie auf Paare die Lust auf Mehr als nur ein Bett haben.
Aufgabenstellung
Bitte an unsere neue Homepage vom Design/Still anpassen: www.trovalin-design.de
Die Broschüre soll als Zulage bei anderen Bestellungen beiliegen und auf Messen verteilt werden.

```html
<!DOCTYPE html>
<html lang="de">
<head>
<meta charset="utf-8">
<title>Trovalin – Broschüre</title>
<link href="https://fonts.googleapis.com/css2?family=Open+Sans:wght@400;600;700&display=swap" rel="stylesheet">
<style>
  :root {
    --backdrop: #5b5b5d;
    --page-dark: #1e1e1e;
    --page-mid: #3a3a3a;
    --ink-light: #ffffff;
    --ink-soft: #c9c9c9;
    --photo-wall: #b3aa9f;
    --photo-shadow: #2b2826;
    --photo-accent: #9e2c1c;
  }
  * { margin: 0; padding: 0; box-sizing: border-box; }
  html, body {
    width: 1200px; height: 781px; overflow: hidden;
    background: var(--backdrop);
    font-family: "Open Sans", Arial, sans-serif;
  }
  .spread {
    position: absolute; left: 100px; top: 40px;
    display: flex; gap: 40px;
  }
  .page {
    position: relative; width: 480px; height: 700px; overflow: hidden;
    box-shadow: 0 12px 30px rgba(0,0,0,.45);
  }
  .cover-front { background: var(--photo-shadow); }
  .cover-photo {
    position: absolute; inset: 0;
    background:
      radial-gradient(ellipse at 40% 70%, rgba(158,44,28,.85) 0%, rgba(158,44,28,0) 35%),
      radial-gradient(ellipse at 75% 30%, rgba(158,44,28,.6) 0%, rgba(158,44,28,0) 30%),
      linear-gradient(160deg, var(--photo-wall) 0%, #8a8178 45%, var(--photo-shadow) 100%);
  }
  .cover-shade {
    position: absolute; inset: 0;
    background: linear-gradient(180deg, rgba(0,0,0,.55) 0%, rgba(0,0,0,0) 22%, rgba(0,0,0,0) 70%, rgba(0,0,0,.75) 100%);
  }
  .brand-name {
    position: absolute; left: 34px; top: 30px;
    display: flex; align-items: center; gap: 10px;
    color: var(--ink-light); font-weight: 700; font-size: 34px; letter-spacing: 2px;
  }
  .brand-dot { width: 14px; height: 14px; border-radius: 50%; background: var(--ink-light); }
  .tagline {
    position: absolute; left: 0; right: 0; bottom: 44px; text-align: center;
    color: var(--ink-light); font-weight: 600; font-size: 21px;
  }
  .cover-back {
    background: linear-gradient(150deg, var(--page-dark) 0%, var(--page-mid) 45%, var(--page-dark) 100%);
  }
  .back-name {
    position: absolute; right: 40px; top: 380px;
    color: var(--ink-light); font-weight: 700; font-size: 52px; letter-spacing: 2px;
  }
  .contact {
    position: absolute; left: 36px; bottom: 60px;
    color: var(--ink-soft); font-size: 13px; line-height: 1.45;
  }
  .contact-row { display: flex; gap: 10px; align-items: flex-start; margin-bottom: 14px; }
  .contact-lines { display: flex; flex-direction: column; }
  .contact-icons { display: flex; flex-direction: column; gap: 3px; padding-top: 2px; }
  .contact-label { color: #8d8d8d; }
  .icon { width: 14px; height: 16px; fill: var(--ink-soft); }
</style>
</head>
<body>
  <main class="spread">
    <section class="page cover-front">
      <div class="cover-photo" role="img" aria-label="Foto: Himmelbett aus Metall mit weißen Vorhängen, roten Satinkissen und geblümter Decke vor gemusterter Tapete"></div>
      <div class="cover-shade"></div>
      <div class="brand-name"><span class="brand-dot"></span>Trovalin</div>
      <p class="tagline">Ihre Wünsche. Ihre Nächte. Ihre Träume.</p>
    </section>

    <section class="page cover-back">
      <div class="back-name">Trovalin</div>
      <address class="contact" style="font-style:normal">
        <div class="contact-row">
          <svg class="icon" viewBox="0 0 14 16"><path d="M7 0a5.5 5.5 0 0 0-5.5 5.5C1.5 10 7 16 7 16s5.5-6 5.5-10.5A5.5 5.5 0 0 0 7 0zm0 7.8a2.3 2.3 0 1 1 0-4.6 2.3 2.3 0 0 1 0 4.6z"/></svg>
          <div class="contact-lines">
            <span class="contact-label">Business premises:</span>
            <span>Lindenweg 12</span>
            <span>D - 69123 Talheim</span>
          </div>
        </div>
        <div class="contact-row">
          <div class="contact-icons">
            <svg class="icon" viewBox="0 0 14 16"><path d="M3 2l2.5 3-1.5 1.5a8 8 0 0 0 4.5 4.5L10 9.5l3 2.5-1.5 2.5C6 14 1 9 1.5 3.5z"/></svg>
            <svg class="icon" viewBox="0 0 14 16"><path d="M1 4h12v9H1z M1 4l6 5 6-5" fill="none" stroke="#c9c9c9" stroke-width="1.4"/></svg>
            <svg class="icon" viewBox="0 0 14 16"><g fill="none" stroke="#c9c9c9" stroke-width="1.2"><circle cx="7" cy="8" r="5.5"/><ellipse cx="7" cy="8" rx="2.4" ry="5.5"/><path d="M1.5 8h11"/></g></svg>
          </div>
          <div class="contact-lines">
            <span>+49 (0) 151 28390417</span>
            <span>service@trovalin-design.de</span>
            <span>www.trovalin-design.de</span>
          </div>
        </div>
      </address>
    </section>
  </main>
</body>
</html>
```